Keelby marketing postcards (6x9)

I would like to replicate this 6x9 postcard, but update name/logo, phone number, web address, etc. I also need to create a second postcard copying this basic design, but with updated content and background pictures. Updated contact info to be used for both postcards:
Website: www.keelbyhomestay.com
Name: Mark Tessler
Email: mtessler@keelbyhomestay.com
Phone: (555) 246-8130

Requirements
Must have
• Need two 6x9 postcard designs; 1 themed for Rivenport College, 1 for Calder State. Have uploaded photos that can be used in design. RC can be used for RC postcard (only), CS can be used for CS (only), Generic can be used for either. I've tried to upload extra photos so that you can use your creativity in selecting those that work best in the design.
Nice to have
• In the "Color palette" file, it has the two color schemes -- one for Rivenport College and one for Calder State. Those respective color schemes should be heavily represented in each design. Then there are different groups of pictures labelled either "CS" or "RC", plus some labelled "Generic". The generic ones can be used in either design, the others should be used only for the design for that school.

```html
<!DOCTYPE html>
<html lang="en">
<head>
<meta charset="utf-8">
<title>Keelby Homestay – Calder State and Rivenport College Postcards</title>
<link href="https://fonts.googleapis.com/css2?family=Alegreya:wght@400;500;700&family=Alegreya+Sans:wght@300;400;500;700&display=swap" rel="stylesheet">
<style>
  :root{
    --stage:#9b9fbb;
    --white:#ffffff;
    --ink:#111111;
    --rule:#333333;
    --cs-panel:rgba(46,140,145,.9);
    --cs-band:#163f73;
    --cs-band-soft:rgba(22,63,115,.92);
    --rc-panel:rgba(176,84,38,.9);
    --rc-band:#3a2a24;
    --rc-band-soft:rgba(58,42,36,.92);
  }
  *{box-sizing:border-box;margin:0;padding:0}
  html,body{width:896px;height:1200px;overflow:hidden;background:var(--stage)}
  body{position:relative;font-family:"Alegreya",serif;color:var(--white)}

  .card{position:absolute;width:732px;height:488px;overflow:hidden;transform:scale(.55);transform-origin:0 0;box-shadow:0 1px 3px rgba(0,0,0,.25)}
  .col-cs{left:31px}
  .col-rc{left:463px}
  .row-front{top:302px}
  .row-back{top:630px}
  .card--back{background:#fff}

  .theme-cs{--panel:var(--cs-panel);--band:var(--cs-band);--band-soft:var(--cs-band-soft)}
  .theme-rc{--panel:var(--rc-panel);--band:var(--rc-band);--band-soft:var(--rc-band-soft)}

  .photo{position:absolute;inset:0}
  .photo--city-night{background:linear-gradient(180deg,#3c6fbf 0%,#7ea2d6 30%,#8fa8c9 44%,#3a4565 62%,#2b3556 74%,#5a4a3e 88%,#2f3a33 100%)}
  .photo--campus-dusk{background:linear-gradient(180deg,#6a7fb8 0%,#c9a98f 34%,#b98a6a 48%,#5b4a48 66%,#3d3a36 82%,#2e3328 100%)}
  .photo--river-day{background:linear-gradient(180deg,#eef2f5 0%,#e6ecef 45%,#cfd8d6 62%,#d9e0e0 75%,#e3e8ea 100%)}
  .photo--lawn-day{background:linear-gradient(180deg,#f2efe9 0%,#ece6dc 45%,#d8dccb 62%,#dfe3d6 78%,#e8e9e2 100%)}

  /* front */
  .intro-panel{position:absolute;left:46px;top:54px;width:282px;height:380px;background:var(--panel);border-radius:6px}
  .intro-panel h2{position:absolute;left:20px;font-weight:700;font-size:22px;letter-spacing:.2px;line-height:24px}
  .intro-panel p{position:absolute;left:22px;width:240px;font-size:15px;line-height:17.6px}
  .brand{position:absolute;left:582px;top:25px;width:104px;text-align:center}
  .brand__mark{display:block;width:16px;height:16px;margin:0 auto 6px;border:1.5px solid var(--white);border-radius:50%}
  .brand__name{font-weight:700;font-size:26px;line-height:1}
  .contact-bar{position:absolute;left:367px;top:357px;width:319px;height:76px;background:var(--band-soft);border-radius:8px}
  .contact-bar__line{position:absolute;right:28px;display:flex;align-items:center;gap:10px;font-family:"Alegreya Sans",sans-serif;font-weight:500;font-size:19px;line-height:1}
  .contact-bar__line svg{width:19px;height:19px}

  /* back */
  .headline-band{position:absolute;left:0;top:0;width:406px;height:89px;background:var(--band);display:flex;align-items:center;justify-content:center;text-align:center}
  .headline-band h1{font-weight:500;font-size:28px;line-height:35px}
  .details-panel{position:absolute;left:0;top:89px;width:406px;height:278px;background:var(--panel);border-bottom-right-radius:10px;font-family:"Alegreya Sans",sans-serif}
  .details-panel .lead{position:absolute;left:46px;top:24px;width:340px;font-weight:700;font-size:15px;line-height:20px}
  .details-panel h2{position:absolute;left:46px;top:88px;font-family:"Alegreya",serif;font-weight:700;font-size:22px;line-height:1}
  .details-panel .rule{position:absolute;left:46px;top:121px;width:106px;height:2px;background:var(--white)}
  .details-panel ul{position:absolute;left:46px;top:131px;width:330px;list-style:none;font-size:17px;line-height:21.7px}
  .details-panel .label{font-weight:300}
  .web-pill{position:absolute;left:55px;top:367px;width:295px;height:47px;background:var(--band);border-radius:0 0 24px 24px;display:flex;align-items:center;justify-content:center;font-size:20px;font-weight:500}
  .postage{position:absolute;left:598px;top:31px;width:88px;height:76px;border:1px solid var(--rule);background:rgba(255,255,255,.9);color:var(--ink);display:flex;align-items:center;justify-content:center;text-align:center;font-size:17px;line-height:22px}
  .address-line{position:absolute;left:435px;width:251px;height:1px;background:var(--rule)}
</style>
</head>
<body>

<!-- Calder State front -->
<section class="card card--front theme-cs col-cs row-front">
  <div class="photo photo--city-night" role="img" aria-label="Evening city skyline over a river with a lit highway bridge"></div>
  <div class="intro-panel">
    <h2 style="top:43px">CALDER STATE FAMILIES</h2>
    <p style="top:79px">Let us help you save thousands on tuition costs</p>
    <p style="top:132px">We have been helping out-of-state families gain Texas residency for Over 14 years.</p>
    <h2 style="top:208px">CONTACT US</h2>
    <p style="top:246px">Contact us to learn how we have helped more than 500 families - and counting - save thousands on tuition.</p>
    <p style="top:318px">Let us help you too.</p>
  </div>
  <div class="brand"><span class="brand__mark"></span><div class="brand__name">Keelby</div></div>
  <div class="contact-bar">
    <div class="contact-bar__line" style="top:14px">
      <svg viewBox="0 0 24 24" fill="#fff" aria-hidden="true"><path d="M6.6 10.8a15.1 15.1 0 0 0 6.6 6.6l2.2-2.2c.3-.3.7-.4 1-.2 1.1.4 2.3.6 3.6.6.6 0 1 .4 1 1V20c0 .6-.4 1-1 1A17 17 0 0 1 3 4c0-.6.4-1 1-1h3.5c.6 0 1 .4 1 1 0 1.3.2 2.5.6 3.6.1.3 0 .7-.2 1z"/></svg>
      <span>(555) 246-8130</span>
    </div>
    <div class="contact-bar__line" style="top:42px">
      <svg viewBox="0 0 24 24" fill="none" stroke="#fff" stroke-width="2" aria-hidden="true"><circle cx="12" cy="12" r="10"/><path d="M2 12h20M12 2c3 3 3 17 0 20M12 2c-3 3-3 17 0 20M4 7h16M4 17h16"/></svg>
      <span>www.keelbyhomestay.com</span>
    </div>
  </div>
</section>

<!-- Rivenport College front -->
<section class="card card--front theme-rc col-rc row-front">
  <div class="photo photo--campus-dusk" role="img" aria-label="Rivenport College campus buildings at dusk"></div>
  <div class="intro-panel">
    <h2 style="top:43px">RIVENPORT COLLEGE<br>FAMILIES</h2>
    <p style="top:103px">Let us help you save thousands on tuition costs</p>
    <p style="top:150px">We have been helping out-of-state families gain Texas residency for Over 14 years.</p>
    <h2 style="top:220px">CONTACT US</h2>
    <p style="top:256px">Contact us to learn how we have helped more than 500 families - and counting - save thousands on tuition.</p>
    <p style="top:324px">Let us help you too.</p>
  </div>
  <div class="brand"><span class="brand__mark"></span><div class="brand__name">Keelby</div></div>
  <div class="contact-bar">
    <div class="contact-bar__line" style="top:14px">
      <svg viewBox="0 0 24 24" fill="#fff" aria-hidden="true"><path d="M6.6 10.8a15.1 15.1 0 0 0 6.6 6.6l2.2-2.2c.3-.3.7-.4 1-.2 1.1.4 2.3.6 3.6.6.6 0 1 .4 1 1V20c0 .6-.4 1-1 1A17 17 0 0 1 3 4c0-.6.4-1 1-1h3.5c.6 0 1 .4 1 1 0 1.3.2 2.5.6 3.6.1.3 0 .7-.2 1z"/></svg>
      <span>(555) 246-8130</span>
    </div>
    <div class="contact-bar__line" style="top:42px">
      <svg viewBox="0 0 24 24" fill="none" stroke="#fff" stroke-width="2" aria-hidden="true"><circle cx="12" cy="12" r="10"/><path d="M2 12h20M12 2c3 3 3 17 0 20M12 2c-3 3-3 17 0 20M4 7h16M4 17h16"/></svg>
      <span>www.keelbyhomestay.com</span>
    </div>
  </div>
</section>

<!-- Calder State back -->
<section class="card card--back theme-cs col-cs row-back">
  <div class="photo photo--river-day" role="img" aria-label="Hazy daytime skyline above a river with paddleboarders and canoes"></div>
  <div class="headline-band"><h1>Let us help you save<br>thousands on tuition costs</h1></div>
  <div class="details-panel">
    <p class="lead">We have been helping out-of-state families gain Texas residency for Over 14 years.</p>
    <h2>CONTACT US</h2>
    <div class="rule"></div>
    <ul>
      <li><span class="label">Mark Tessler , Keelby Homestay</span></li>
      <li><span class="label">Phone : </span>(555) 246-8130</li>
      <li><span class="label">Email : </span>mtessler@keelbyhomestay.com</li>
      <li><span class="label">Address : </span>418 Harbor Lane, Suite 2, Rivenport, TX 78701</li>
    </ul>
  </div>
  <div class="web-pill">www.keelbyhomestay.com</div>
  <div class="postage">Postage<br>Area</div>
  <div class="address-line" style="top:235px"></div>
  <div class="address-line" style="top:286px"></div>
  <div class="address-line" style="top:338px"></div>
</section>

<!-- Rivenport College back -->
<section class="card card--back theme-rc col-rc row-back">
  <div class="photo photo--lawn-day" role="img" aria-label="Sunny campus lawn with students walking under trees"></div>
  <div class="headline-band"><h1>Let us help you save<br>thousands on tuition costs</h1></div>
  <div class="details-panel">
    <p class="lead">We have been helping out-of-state families gain Texas residency for Over 14 years.</p>
    <h2>CONTACT US</h2>
    <div class="rule"></div>
    <ul>
      <li><span class="label">Mark Tessler , Keelby Homestay</span></li>
      <li><span class="label">Phone : </span>(555) 246-8130</li>
      <li><span class="label">Email : </span>mtessler@keelbyhomestay.com</li>
      <li><span class="label">Address : </span>418 Harbor Lane, Suite 2, Rivenport, TX 78701</li>
    </ul>
  </div>
  <div class="web-pill">www.keelbyhomestay.com</div>
  <div class="postage">Postage<br>Area</div>
  <div class="address-line" style="top:235px"></div>
  <div class="address-line" style="top:286px"></div>
  <div class="address-line" style="top:338px"></div>
</section>

</body>
</html>
```